Business start up

I need a logo within the business cards that has the name brixol with two racing stripes like the halvor racing stripes next to the name .... one of the stripes I would want to have the shades of window tint and the other stripe the colors of vinyl wrap or even the name having dripping paint of the different colors in it ... it will be a business of window tint and vinyl wrap .... service that I will be providing would be window tint Vinyl wrap Paint protection (ppfTaillights/headlights tintsBlackouts/Chrome delete Decals

Target Market(s)

Automotive

Industry/Entity Type

Automotive

Contact Information for Business Card

Have the name brixo drip like paint and have different colors dripping

Font styles to use
Serif
Sans Serif
Decorative
Script

Colors

Designer to choose colors to be used in the design.

Requirements
Nice to have
• I need a logo within the business cards that has the name brixol with two racing stripes like the halvor racing stripes next to the name .... one of the stripes I would want to have the shades of window tint and the other stripe the colors of vinyl wrap or even the name having dripping paint of the different colors in it ... it will be a business of window tint and vinyl wrap .... service that I will be providing would be
• window tint
• Vinyl wrap
• Paint protection (ppf
• Taillights/headlights tints
• Blackouts/Chrome delete
• Decals

```html
<!DOCTYPE html>
<html lang="en">
<head>
<meta charset="utf-8">
<title>Brixol Business Cards</title>
<link rel="stylesheet" href="https://fonts.googleapis.com/css2?family=Audiowide&display=swap">
<style>
  :root {
    --backdrop: #1c1c1d;
    --card: #121314;
    --stripe-yellow: #e8d35f;
    --accent-blue: #2f62c4;
    --ink-dark: #141414;
  }
  * { margin: 0; padding: 0; box-sizing: border-box; }
  html, body {
    width: 1200px; height: 900px; overflow: hidden;
    background: var(--backdrop);
    font-family: "Audiowide", sans-serif;
  }
  .card {
    position: absolute; left: 250px;
    width: 700px; height: 400px;
    background: var(--card);
    overflow: hidden;
  }
  .card--front { top: 40px; }
  .card--back { top: 465px; }

  .brand-name {
    color: var(--accent-blue);
    font-family: "Audiowide", sans-serif;
    font-weight: 400;
    letter-spacing: 4px;
    text-transform: uppercase;
    line-height: 1;
  }
  .card--front .brand-name {
    position: absolute; top: 110px; left: 0; width: 100%;
    text-align: center; font-size: 72px;
  }
  .card--back .brand-name {
    position: absolute; top: 48px; left: 40px; font-size: 54px;
  }

  .services {
    position: absolute; left: 40px; right: 40px; top: 255px;
    color: var(--stripe-yellow);
    font-size: 13px; letter-spacing: 1.2px;
    text-transform: uppercase; line-height: 2;
  }
  .services ul { list-style: none; display: flex; flex-wrap: wrap; column-gap: 14px; }
  .services li::before {
    content: ""; display: inline-block; width: 5px; height: 5px;
    background: var(--accent-blue); margin-right: 6px; vertical-align: middle;
  }

  .stripes { position: absolute; left: 0; top: 0; }
  .stripe { fill: var(--stripe-yellow); }

  .holder-name {
    position: absolute; left: 60px; top: 208px;
    color: var(--ink-dark); font-size: 18px; letter-spacing: 1px;
    text-transform: uppercase;
  }

  .contact {
    position: absolute; left: 40px; top: 305px;
    list-style: none; color: var(--stripe-yellow);
    font-size: 17px; letter-spacing: 1.5px; line-height: 1.9;
  }
  .contact li { display: flex; align-items: center; gap: 12px; }
  .contact svg { width: 16px; height: 16px; fill: none; stroke: var(--accent-blue); stroke-width: 1.6; }
  .contact .icon-phone { fill: var(--accent-blue); stroke: none; }
</style>
</head>
<body>

<section class="card card--front">
  <div class="brand-name">Brixol</div>
  <div class="services">
    <ul>
      <li>Window Tint</li>
      <li>Vinyl Wrap</li>
      <li>Paint Protection (PPF</li>
      <li>Taillights/Headlights Tints</li>
      <li>Blackouts/Chrome Delete</li>
      <li>Decals</li>
    </ul>
  </div>
</section>

<section class="card card--back">
  <div class="brand-name">Brixol</div>

  <svg class="stripes" width="700" height="400" viewBox="0 0 700 400">
    <polygon class="stripe stripe--name" points="0,190 335,190 300,250 0,250"/>
    <polygon class="stripe stripe--run" points="360,212 700,212 700,272 325,272"/>
  </svg>

  <div class="holder-name">Marco</div>

  <ul class="contact">
    <li>
      <svg class="icon-phone" viewBox="0 0 16 16"><path d="M3.2 1.5l2.3 0 1 3.2-1.5 1.2c.8 1.8 2.3 3.3 4.1 4.1l1.2-1.5 3.2 1v2.3c0 .7-.6 1.2-1.3 1.2C6.8 13 3 9.2 2 3.5c0-.9.5-2 1.2-2z"/></svg>
      <span>(555) 014/2273</span>
    </li>
    <li>
      <svg viewBox="0 0 16 16"><rect x="1.5" y="3.5" width="13" height="9"/><path d="M1.5 3.5l6.5 5 6.5-5"/></svg>
      <span>312.brixol@ail.com</span>
    </li>
  </ul>
</section>

</body>
</html>
```